vel-nory needs updated company presentation for perspective principals

We are looking to update our current company overview presentation that we use for giving new and prospective principals (companies we see for) an overview of our company and our capabilities. We have a PowerPoint presentation but would like to give it a more professional and updated look. There are some modification we'd like to incorporate into the new presentation, but that can be added later.
We will also be looking at using this look to update our website and some additional promotion literature for the near future ( Brochures, Mailers....)
Updates

On the territory overview. I need to increase the state view to include Missouri, Iowa, Kansas, Nebraska, Minnesota and Tennessee. This is the first project we've worked on, so please let me know what additional information is required or makes this process go smoother.

Industry/Entity Type

Chemical Product

Font styles to use
Serif

Colors
ec1f27
000000

Requirements
Must have
• Company History, Territory overview, Industries Served, Principal Represented, Employee overview, Historic Performance

```html
<!DOCTYPE html>
<html lang="en">
<head>
<meta charset="utf-8">
<title>vel-nory, inc. — company presentation pages</title>
<link rel="stylesheet" href="https://fonts.googleapis.com/css2?family=Open+Sans:wght@400;600;700;800&display=swap">
<style>
  :root {
    --brand-red: #ec1f27;
    --brand-black: #000000;
    --band-black: #0d0d0d;
    --sheet-grey: #e4e4e4;
    --page-white: #ffffff;
    --text-white: #ffffff;
    --label-ink: #1a1a1a;
  }
  * { margin: 0; padding: 0; box-sizing: border-box; }
  html, body { width: 1200px; height: 1025px; overflow: hidden; }
  body {
    background: var(--sheet-grey);
    font-family: "Open Sans", Arial, sans-serif;
    position: relative;
  }
  .page {
    position: absolute;
    width: 562px;
    height: 421px;
    background: var(--page-white);
    box-shadow: 0 2px 6px rgba(0,0,0,0.25);
    overflow: hidden;
  }
  .page svg { display: block; width: 562px; height: 421px; }
  .page--cover { left: 22px; top: 42px; }
  .page--philosophy { left: 614px; top: 42px; }
  .page--about { left: 22px; top: 530px; }
  .page--contact { left: 614px; top: 530px; }
  .page-label {
    position: absolute;
    width: 562px;
    text-align: center;
    font-size: 17px;
    font-weight: 600;
    color: var(--label-ink);
    letter-spacing: 0.3px;
  }
  .page-label--cover { left: 22px; top: 477px; }
  .page-label--philosophy { left: 614px; top: 477px; }
  .page-label--about { left: 22px; top: 966px; }
  .page-label--contact { left: 614px; top: 966px; }

  .wordmark { font-family: "Open Sans", Arial, sans-serif; font-weight: 800; fill: var(--brand-black); }
  .menu-item { font-weight: 700; font-size: 14px; fill: var(--brand-red); }
  .site-url { font-size: 9px; letter-spacing: 3px; }
  .site-url--light { fill: var(--text-white); }
  .site-url--red { fill: var(--brand-red); }
  .section-title { font-weight: 700; fill: var(--brand-red); }
  .body-copy { font-size: 7.4px; fill: var(--text-white); }
  .fact { font-size: 8.4px; fill: var(--text-white); }
  .contact-title { font-weight: 700; font-size: 29px; fill: var(--brand-red); }
  .contact-line { font-size: 14px; fill: var(--text-white); }
  .fill-red { fill: var(--brand-red); }
  .fill-black { fill: var(--brand-black); }
  .fill-band { fill: var(--band-black); }
  .stroke-white { stroke: var(--text-white); }
  .stroke-red { stroke: var(--brand-red); }
</style>
</head>
<body>

<!-- Cover page -->
<div class="page page--cover">
  <svg viewBox="0 0 702 527" aria-label="Cover page">
    <defs>
      <linearGradient id="handsTone" x1="0" y1="0" x2="1" y2="1">
        <stop offset="0" stop-color="#e9e6e2"/>
        <stop offset="0.5" stop-color="#8a6248"/>
        <stop offset="1" stop-color="#d9d4cf"/>
      </linearGradient>
    </defs>
    <rect class="fill-band" x="0" y="389" width="702" height="138"/>
    <polygon class="fill-red" points="702,78 528,252 573,297 702,168"/>
    <polygon role="img" aria-label="Photo of four hands joined in a team fist bump" fill="url(#handsTone)" points="425,148 572,295 425,442 278,295"/>
    <polygon class="fill-black" points="479,108 527,156 479,204 431,156"/>
    <polygon class="fill-red" points="275,205 323,253 275,301 227,253"/>
    <text class="wordmark" x="26" y="72" font-size="58">vel-nory, inc.</text>
    <g>
      <circle class="fill-black" cx="33" cy="177" r="6"/>
      <path d="M30 177 l2 2 l4 -4" class="stroke-white" stroke-width="1.5" fill="none"/>
      <text class="menu-item" x="48" y="182">ABOUT US</text>
      <circle class="fill-black" cx="33" cy="224" r="6"/>
      <path d="M30 224 l2 2 l4 -4" class="stroke-white" stroke-width="1.5" fill="none"/>
      <text class="menu-item" x="48" y="229">SALES</text>
      <circle class="fill-black" cx="33" cy="271" r="6"/>
      <path d="M30 271 l2 2 l4 -4" class="stroke-white" stroke-width="1.5" fill="none"/>
      <text class="menu-item" x="48" y="276">SYSTEMS &amp; LOGISTICS</text>
      <circle class="fill-black" cx="33" cy="319" r="6"/>
      <path d="M30 319 l2 2 l4 -4" class="stroke-white" stroke-width="1.5" fill="none"/>
      <text class="menu-item" x="48" y="324">PATH TO SUCCESS</text>
    </g>
    <g class="stroke-white" stroke-width="1" fill="none">
      <line x1="203" y1="497" x2="275" y2="497"/>
      <line x1="430" y1="497" x2="500" y2="497"/>
      <circle cx="201" cy="497" r="2"/>
      <circle cx="502" cy="497" r="2"/>
    </g>
    <text class="site-url site-url--light" x="351" y="500" text-anchor="middle">www.vel-noryinc.com</text>
  </svg>
</div>
<div class="page-label page-label--cover">COVER PAGE</div>

<!-- Page 01: philosophy -->
<div class="page page--philosophy">
  <svg viewBox="0 0 702 527" aria-label="Philosophy page">
    <defs>
      <linearGradient id="laptopTone" x1="0" y1="0" x2="1" y2="1">
        <stop offset="0" stop-color="#d8c3a0"/>
        <stop offset="0.45" stop-color="#2a68b8"/>
        <stop offset="1" stop-color="#a47544"/>
      </linearGradient>
    </defs>
    <rect class="fill-band" x="0" y="180" width="702" height="144"/>
    <polygon role="img" aria-label="Photo of a laptop on a desk with a hand holding a globe on screen" fill="url(#laptopTone)" points="175,105 320,250 175,395 30,250"/>
    <polygon class="fill-black" points="122,51 170,99 122,147 74,99"/>
    <polygon class="fill-red" points="221,365 269,413 221,461 173,413"/>
    <text class="wordmark" x="676" y="46" font-size="24" text-anchor="end">vel-nory, inc.</text>
    <text class="section-title" x="329" y="204" font-size="10">VEL-NORY PHILOSOPHY</text>
    <line x1="331" y1="210" x2="331" y2="304" class="stroke-white" stroke-width="1"/>
    <text class="body-copy" x="340" y="224">vel-nory is successful when we partner with quality manufactures to bring unique chemistries</text>
    <text class="body-copy" x="340" y="237">to a customer base that we have strong, long-term relationships with, enabling success for all.</text>
    <text class="body-copy" x="340" y="257">We focus on growth executing our principals missions, acting as an extension of their sale team.</text>
    <text class="body-copy" x="340" y="270">Knowing that if we help them achieve their goals the opportunity to expand with them increases</text>
    <text class="body-copy" x="340" y="283">( Corvane, Halbeck, Trimora...)</text>
    <text class="body-copy" x="340" y="302">Focus on long-term relationship and strategic growth based off execution.</text>
    <g class="stroke-red" stroke-width="1" fill="none">
      <line x1="203" y1="497" x2="275" y2="497"/>
      <line x1="430" y1="497" x2="500" y2="497"/>
      <circle cx="201" cy="497" r="2"/>
      <circle cx="502" cy="497" r="2"/>
    </g>
    <text class="site-url site-url--red" x="351" y="500" text-anchor="middle">www.vel-noryinc.com</text>
  </svg>
</div>
<div class="page-label page-label--philosophy">PAGE - 01</div>

<!-- Page 02: about the company -->
<div class="page page--about">
  <svg viewBox="0 0 702 527" aria-label="About the company page">
    <defs>
      <linearGradient id="towerTone" x1="0" y1="0" x2="0" y2="1">
        <stop offset="0" stop-color="#6f95c9"/>
        <stop offset="0.55" stop-color="#b9c3cc"/>
        <stop offset="1" stop-color="#7b7466"/>
      </linearGradient>
    </defs>
    <polygon class="fill-black" points="0,0 62,0 0,62"/>
    <polygon class="fill-black" points="0,62 62,0 31,62 0,62" opacity="0"/>
    <rect class="fill-band" x="0" y="89" width="702" height="361"/>
    <rect role="img" aria-label="Photo of a tall office tower on a city plaza" fill="url(#towerTone)" x="28" y="75" width="264" height="386"/>
    <polygon class="fill-red" points="702,458 702,527 633,527"/>
    <text class="wordmark" x="676" y="46" font-size="24" text-anchor="end">vel-nory, inc.</text>
    <text class="section-title" x="323" y="118" font-size="11">ABOUT THE COMPANY</text>
    <g class="fill-white">
      <circle cx="330" cy="136" r="3" fill="#fff"/><circle cx="330" cy="155" r="3" fill="#fff"/>
      <circle cx="330" cy="175" r="3" fill="#fff"/><circle cx="330" cy="194" r="3" fill="#fff"/>
      <circle cx="330" cy="214" r="3" fill="#fff"/><circle cx="330" cy="233" r="3" fill="#fff"/>
      <circle cx="330" cy="351" r="3" fill="#fff"/>
      <circle cx="366" cy="253" r="1.5" fill="#fff"/><circle cx="366" cy="272" r="1.5" fill="#fff"/>
      <circle cx="366" cy="292" r="1.5" fill="#fff"/><circle cx="366" cy="311" r="1.5" fill="#fff"/>
      <circle cx="366" cy="331" r="1.5" fill="#fff"/><circle cx="366" cy="370" r="1.5" fill="#fff"/>
      <circle cx="366" cy="403" r="1.5" fill="#fff"/><circle cx="366" cy="423" r="1.5" fill="#fff"/>
    </g>
    <text class="fact" x="340" y="139">vel-nory was founded in 1951</text>
    <text class="fact" x="340" y="158">Headquartered in Cleveland Ohio</text>
    <text class="fact" x="340" y="178">We are currently in our fourth generation of ownership</text>
    <text class="fact" x="340" y="197">Privately held corporation with 6 principal owners</text>
    <text class="fact" x="340" y="217">Strongest financial position in the company's 67 year history.</text>
    <text class="fact" x="340" y="236">Management team</text>
    <text class="fact" x="371" y="256">Alan Whitcombe – President</text>
    <text class="fact" x="371" y="275">Ross Delany – Vice President</text>
    <text class="fact" x="371" y="295">Neil Hartung – CFO</text>
    <text class="fact" x="371" y="314">Gary Lothrop – Senior Vice President</text>
    <text class="fact" x="371" y="334">Dean Morrow – Vice President of Sales</text>
    <text class="fact" x="340" y="354">18 total employees ( most in company history )</text>
    <text class="fact" x="371" y="373">11 sales people ( averaging 17 years of experience in the industry, 11 years on</text>
    <text class="fact" x="371" y="387">average at vel-nory while adding three new employees in the last 12 months )</text>
    <text class="fact" x="371" y="406">3 Customer Service Representatives – Avg. 18 years with vel-nory.</text>
    <text class="fact" x="371" y="426">Operations – Avg. 14 years experience at vel-nory.</text>
    <g class="stroke-red" stroke-width="1" fill="none">
      <line x1="203" y1="497" x2="275" y2="497"/>
      <line x1="430" y1="497" x2="500" y2="497"/>
      <circle cx="201" cy="497" r="2"/>
      <circle cx="502" cy="497" r="2"/>
    </g>
    <text class="site-url site-url--red" x="351" y="500" text-anchor="middle">www.vel-noryinc.com</text>
  </svg>
</div>
<div class="page-label page-label--about">PAGE - 02</div>

<!-- Back page: contact -->
<div class="page page--contact">
  <svg viewBox="0 0 702 527" aria-label="Contact page">
    <defs>
      <linearGradient id="skylineTone" x1="0" y1="0" x2="0" y2="1">
        <stop offset="0" stop-color="#0d0d0d" stop-opacity="0"/>
        <stop offset="1" stop-color="#0d0d0d"/>
      </linearGradient>
    </defs>
    <rect role="img" aria-label="City skyline silhouette" fill="url(#skylineTone)" x="0" y="182" width="702" height="30"/>
    <rect class="fill-band" x="0" y="211" width="702" height="316"/>
    <text class="wordmark" x="351" y="106" font-size="54" text-anchor="middle">vel-nory, inc.</text>
    <text class="contact-title" x="351" y="283" text-anchor="middle">CONTACT US</text>
    <line x1="267" y1="293" x2="435" y2="293" class="stroke-red" stroke-width="1.5"/>
    <circle cx="327" cy="319" r="7" fill="#fff"/>
    <path d="M327 323 c-3 -3.5 -3 -5 -3 -6 a3 3 0 0 1 6 0 c0 1 0 2.5 -3 6z" class="fill-black"/>
    <circle cx="351" cy="319" r="7" fill="#fff"/>
    <path d="M348 315 l2 -0.5 l1 2.5 l-1.2 1 a5 5 0 0 0 2.2 2.2 l1 -1.2 l2.5 1 l-0.5 2 c-4 0 -7 -3 -7 -7z" class="fill-black"/>
    <circle cx="375" cy="319" r="7" fill="#fff"/>
    <rect x="372" y="316" width="6" height="6" class="fill-black"/>
    <rect x="373.5" y="314" width="3" height="2" class="fill-black"/>
    <text class="contact-line" x="351" y="357" text-anchor="middle">2470 Alder Crest Drive, Birchfield, OH  44190</text>
    <text class="contact-line" x="351" y="393" text-anchor="middle">216-555-0176</text>
    <text class="contact-line" x="351" y="429" text-anchor="middle">216-555-0189</text>
    <g class="stroke-white" stroke-width="1" fill="none">
      <line x1="203" y1="497" x2="275" y2="497"/>
      <line x1="430" y1="497" x2="500" y2="497"/>
      <circle cx="201" cy="497" r="2"/>
      <circle cx="502" cy="497" r="2"/>
    </g>
    <text class="site-url site-url--light" x="351" y="500" text-anchor="middle">www.vel-noryinc.com</text>
  </svg>
</div>
<div class="page-label page-label--contact">BACK PAGE</div>

</body>
</html>
```